Anti Cellulite Treatment Massage Oil see link https://www.brindlemart.com/Anti-Cellulite-Treatment-Massa

i need a packaging design for Anti Cellulite Treatment Massage Oil like this
https://www.brindlemart.com/s/ref=nb_sb_noss?url=search-alias%3Daps&field-keywords=Anti+Cellulite+Treatment+Massage+Oil+

our company is talo see link below https://www.brindlemart.com/Tal%C3%B6-Beauty-Garcinia-Cambogia-Extract/dp/K73QX2M9R5/ref=sr_1_1_a_it?ie=UTF8&qid=1494884000&sr=8-1&keywords=talo

its a 8oz / 240 ml

Target Market(s)

health & beauty

Industry/Entity Type

Massage

Font styles to use
Serif
Sans Serif
Decorative
Script

Colors

Designer to choose colors to be used in the design.

Requirements
Must have
• our logo and pump like this seller
• https://www.brindlemart.com/Anti-Cellulite-Treatment-Massage-Oil/dp/K94RT6P2W8/ref=sr_1_1_a_it?ie=UTF8&qid=1494884194&sr=8-1&keywords=+Anti+Cellulite+Treatment+Massage+Oil
Nice to have
• the most similar to this or even better idea from this link
Should not have
• pictures on the label

```html
<!DOCTYPE html>
<html lang="en">
<head>
<meta charset="UTF-8">
<title>talo Anti Cellulite Massage Oil — Label</title>
<link href="https://fonts.googleapis.com/css2?family=Lato:wght@300;400;700;900&family=Zilla+Slab:wght@300;400&display=swap" rel="stylesheet">
<style>
  :root {
    --page: #ffffff;
    --label: #2c2f31;
    --olive: #b3b25e;
    --white: #f4f4f4;
    --band-text: #2c2f31;
    --figure: #3a3d36;
  }
  * { margin: 0; padding: 0; box-sizing: border-box; }
  html, body {
    width: 1200px; height: 1200px; overflow: hidden;
    background: var(--page);
  }
  .label {
    position: absolute;
    left: 250px; top: 125px;
    width: 700px; height: 950px;
    background: var(--label);
    font-family: "Lato", sans-serif;
  }
  .title-main {
    position: absolute;
    left: 50px; top: 118px;
    width: 100px;
    writing-mode: vertical-rl;
    transform: rotate(180deg);
    color: var(--white);
    font-weight: 700;
    font-size: 100px;
    line-height: 100px;
    letter-spacing: 1px;
    white-space: nowrap;
  }
  .title-band {
    position: absolute;
    left: 148px; top: 220px;
    width: 68px; height: 720px;
    background: var(--olive);
  }
  .title-band span {
    position: absolute;
    left: 0; top: 18px;
    width: 68px;
    writing-mode: vertical-rl;
    transform: rotate(180deg);
    color: var(--band-text);
    font-weight: 300;
    font-size: 74px;
    line-height: 68px;
    letter-spacing: 2px;
    white-space: nowrap;
  }
  .brand {
    position: absolute;
    left: 238px; top: 148px;
    display: flex; align-items: center; gap: 30px;
  }
  .brand-mark {
    width: 70px; height: 70px;
    border: 6px solid var(--olive);
    border-radius: 50%;
  }
  .brand-name {
    color: var(--white);
    font-weight: 400;
    font-size: 52px;
    letter-spacing: 8px;
    line-height: 1;
  }
  .dots {
    position: absolute;
    left: 246px; width: 398px;
    border-top: 4px dotted var(--white);
  }
  .dots.top { top: 251px; }
  .dots.bottom { top: 374px; }
  .purity {
    position: absolute;
    left: 246px; top: 284px;
    color: var(--white);
    font-family: "Zilla Slab", serif;
    font-weight: 300;
    font-size: 42px;
    line-height: 44px;
    letter-spacing: 1px;
  }
  .benefits {
    position: absolute;
    left: 246px; top: 412px;
    color: var(--white);
    font-size: 21px;
    letter-spacing: 0.5px;
    display: flex; align-items: center; gap: 8px;
  }
  .benefits .dot {
    width: 16px; height: 16px;
    border: 2px solid var(--white);
    border-radius: 50%;
  }
  .figure-art {
    position: absolute;
    left: 456px; top: 533px;
    width: 188px; height: 397px;
    background: linear-gradient(180deg, var(--figure), var(--label));
  }
</style>
</head>
<body>
  <main class="label">
    <h1 class="title-main">ANTI CELLULITE</h1>
    <div class="title-band"><span>MASSAGE OIL</span></div>

    <div class="brand">
      <div class="brand-mark"></div>
      <div class="brand-name">TALO</div>
    </div>

    <div class="dots top"></div>
    <p class="purity">100% PURE<br>NATURAL</p>
    <div class="dots bottom"></div>

    <p class="benefits"><span class="dot"></span>FIRMS.MOISTURIZES.TONES<span class="dot"></span></p>

    <div class="figure-art" role="img" aria-label="Olive line drawing of a female body silhouette with arm raised"></div>
  </main>
</body>
</html>
```